Biz Card Physical Therapy Company
Lorimer Physical Therapy
Bright & Fun-filled
Darnell Okoro, PT, CIMT, CSCS
Director
4172 W Fenwick Ave,
Harbor Vale, CA 90812
LorimerTherapy@quillpost.com
CA PT 61803
Please feel free to move the logo to the side of the tag-line, or however you may see fit
vector logo file

```html
<!DOCTYPE html>
<html lang="en">
<head>
<meta charset="utf-8">
<title>Lorimer Physical Therapy – Business Card</title>
<link rel="stylesheet" href="https://fonts.googleapis.com/css2?family=Montserrat:ital,wght@0,400;0,600;0,800;1,600&display=swap">
<style>
  :root {
    --stage: #2b2b2d;
    --card-white: #f7f7f7;
    --card-shade: #e4e4e4;
    --green-light: #6e9a3a;
    --green-dark: #2f5a16;
    --brand-green: #4e8a2a;
    --brand-purple: #8a3f93;
    --divider: #151515;
    --icon-cut: #3f6e22;
  }
  * { margin: 0; padding: 0; box-sizing: border-box; }
  html, body { width: 1200px; height: 901px; overflow: hidden; }
  body {
    background: var(--stage);
    font-family: "Montserrat", Arial, sans-serif;
    position: relative;
  }
  .card {
    position: absolute;
    left: 290px;
    width: 620px;
    height: 354px;
    border-radius: 18px;
    overflow: hidden;
    background: linear-gradient(135deg, var(--card-white) 0%, #ffffff 45%, var(--card-shade) 100%);
  }
  .card--back { top: 71px; }
  .card--front { top: 475px; display: flex; }

  /* back */
  .back-mark {
    position: absolute;
    left: 40px; top: 60px;
    font-weight: 800;
    font-size: 64px;
    line-height: 1.05;
    color: var(--brand-green);
    opacity: 0.12;
    text-transform: uppercase;
  }

  /* front */
  .brand-side {
    width: 352px;
    height: 100%;
    display: flex;
    flex-direction: column;
    align-items: center;
    justify-content: center;
    padding: 0 20px;
  }
  .brand-name {
    display: flex;
    align-items: center;
    gap: 10px;
    color: var(--brand-green);
    font-weight: 800;
    text-transform: uppercase;
    line-height: 1.05;
  }
  .brand-square {
    width: 26px; height: 26px;
    background: var(--brand-green);
    flex: none;
  }
  .brand-lines { display: flex; flex-direction: column; }
  .brand-lines .top { font-size: 34px; letter-spacing: 1px; }
  .brand-lines .bottom { font-size: 19px; letter-spacing: 0.5px; }
  .tagline {
    margin-top: 10px;
    font-style: italic;
    font-weight: 600;
    font-size: 12.5px;
    color: var(--brand-purple);
    letter-spacing: 0.3px;
  }
  .divider {
    width: 8px;
    height: 100%;
    background: var(--divider);
  }
  .info-side {
    flex: 1;
    height: 100%;
    background: linear-gradient(160deg, var(--green-light) 0%, var(--green-dark) 100%);
    color: #ffffff;
    padding: 30px 20px 24px 22px;
    display: flex;
    flex-direction: column;
    justify-content: space-between;
  }
  .person-name { font-size: 14px; font-weight: 600; }
  .person-title { font-size: 11.5px; margin-top: 3px; }
  .contact { font-size: 11.5px; line-height: 1.55; }
  .contact .address { margin-bottom: 8px; }
  .contact-row { display: flex; align-items: center; gap: 7px; }
  .contact-row svg { width: 11px; height: 11px; flex: none; }
</style>
</head>
<body>
  <section class="card card--back" aria-label="Card back">
    <div class="back-mark">Lorimer<br>Physical<br>Therapy</div>
  </section>

  <section class="card card--front" aria-label="Card front">
    <div class="brand-side">
      <div class="brand-name">
        <span class="brand-square"></span>
        <span class="brand-lines">
          <span class="top">Lorimer</span>
          <span class="bottom">Physical Therapy</span>
        </span>
      </div>
      <p class="tagline">Recovery, Strength &amp; Motion</p>
    </div>
    <div class="divider"></div>
    <div class="info-side">
      <div class="person">
        <p class="person-name">Darnell Okoro, PT, CIMT, CSCS</p>
        <p class="person-title">Director</p>
      </div>
      <div class="contact">
        <p class="address">4172 W Fenwick Ave<br>Harbor Vale, CA 90812</p>
        <p class="contact-row">
          <svg viewBox="0 0 12 12" aria-hidden="true"><path d="M2 1h3l1 3-1.5 1a6 6 0 0 0 2.5 2.5L8 6l3 1v3c0 .6-.4 1-1 1A9 9 0 0 1 1 2c0-.6.4-1 1-1z" fill="#fff"/></svg>
          (562) 555-0187
        </p>
        <p class="contact-row">
          <svg viewBox="0 0 12 12" aria-hidden="true"><rect x="3" y="0.5" width="6" height="11" rx="1.2" fill="#fff"/><rect x="4" y="2" width="4" height="6.5" fill="var(--icon-cut)"/></svg>
          (562) 555-0143
        </p>
        <p class="contact-row">
          <svg viewBox="0 0 12 12" aria-hidden="true"><rect x="0.5" y="2" width="11" height="8" rx="1" fill="#fff"/><path d="M1 2.5l5 4 5-4" stroke="var(--icon-cut)" stroke-width="1" fill="none"/></svg>
          LorimerTherapy@quillpost.com
        </p>
      </div>
    </div>
  </section>
</body>
</html>
```